A Leisure SPA Plaza Hotel needs Creative VIP Cards Design

We need VIP Cards Design for a SPA Plaza Hotel, This leisure SPA plaza hotel have multiple sub projects, such as leisure hotel room, large buffet restaurant, swimming pool, theatrical performances, sauna bath, massage, SPA, Tea bar, 3D cinema, KTV rooms, chess room, Internet cafes , art appreciation, children's Castle, Korean geothermal, table tennis, billiard room, GYM and other entertainments.
We need Three creative VIP Card design for 3 different level:
1. Golden Card
2. Platinum Card
3. Diamond Card
Attached, Please find the LOGO file and some sample, we new design with much better look than those samples.

```html
<!DOCTYPE html>
<html lang="en">
<head>
<meta charset="utf-8">
<title>VIP Membership Cards – Bright Cove Leisure Plaza</title>
<link rel="stylesheet" href="https://fonts.googleapis.com/css2?family=Tinos:wght@400;700&display=swap">
<style>
  :root {
    --stage: #000000;
    --brand-teal: #2a98b6;
    --brand-sun: #f2b545;

    --gold-top: #c4873c;
    --gold-mid: #b7a634;
    --gold-bottom: #f6c063;
    --gold-ink: #3c2314;
    --gold-band: rgba(255, 250, 225, 0.72);

    --platinum-top: #2e2e2e;
    --platinum-mid: #7c7c7c;
    --platinum-bottom: #5a5a5a;
    --platinum-ink: #ffffff;
    --platinum-band: rgba(240, 240, 240, 0.82);

    --diamond-top: #7d8d99;
    --diamond-mid: #0e70a8;
    --diamond-bottom: #1f3d9c;
    --diamond-ink: #ffffff;
    --diamond-band: rgba(205, 235, 245, 0.8);
  }

  * { box-sizing: border-box; margin: 0; padding: 0; }

  html, body {
    width: 1200px;
    height: 1200px;
    overflow: hidden;
    background: var(--stage);
  }

  .card-set {
    position: relative;
    width: 1200px;
    height: 1200px;
  }

  .vip-card {
    position: absolute;
    container-type: size;
    border-radius: 26px;
    overflow: hidden;
    color: var(--ink);
    background: linear-gradient(180deg, var(--top) 0%, var(--mid) 52%, var(--bottom) 100%);
  }

  .vip-card--gold     { left: 408px; top: 54px;  width: 394px; height: 664px;
    --top: var(--gold-top); --mid: var(--gold-mid); --bottom: var(--gold-bottom);
    --ink: var(--gold-ink); --band: var(--gold-band); }
  .vip-card--platinum { left: 49px;  top: 565px; width: 335px; height: 563px;
    --top: var(--platinum-top); --mid: var(--platinum-mid); --bottom: var(--platinum-bottom);
    --ink: var(--platinum-ink); --band: var(--platinum-band); }
  .vip-card--diamond  { left: 828px; top: 565px; width: 332px; height: 557px;
    --top: var(--diamond-top); --mid: var(--diamond-mid); --bottom: var(--diamond-bottom);
    --ink: var(--diamond-ink); --band: var(--diamond-band); }

  /* diagonal light bands */
  .vip-card::before {
    content: "";
    position: absolute;
    inset: 0;
    background: repeating-linear-gradient(135deg,
      rgba(255,255,255,0.10) 0 34px,
      rgba(255,255,255,0) 34px 68px);
  }

  .flourish-field {
    position: absolute;
    inset: 0;
    background:
      radial-gradient(ellipse 45% 35% at 85% 62%, rgba(255,255,255,0.16), transparent 70%),
      radial-gradient(ellipse 40% 30% at 15% 75%, rgba(255,255,255,0.12), transparent 70%);
  }

  .ornament {
    position: absolute;
    left: 12.5%;
    width: 75%;
    height: 6.5%;
    background: linear-gradient(90deg, transparent, var(--ink) 30%, var(--ink) 70%, transparent);
    opacity: 0.45;
    border-radius: 50%;
  }
  .ornament--top    { top: 5%; }
  .ornament--bottom { top: 88.5%; }

  .brand-band {
    position: absolute;
    left: 0;
    right: 0;
    top: 20.3%;
    height: 26.8%;
    background: var(--band);
    display: flex;
    flex-direction: column;
    align-items: center;
    justify-content: center;
    gap: 3.5cqh;
  }

  .brand-dot {
    width: 9cqh;
    height: 9cqh;
    border-radius: 50%;
    background: var(--brand-sun);
  }

  .brand-name {
    font-family: "Tinos", "Times New Roman", serif;
    font-weight: 400;
    font-size: 4.6cqh;
    letter-spacing: 0.02em;
    color: var(--brand-teal);
    white-space: nowrap;
  }

  .tier-mark {
    position: absolute;
    left: 0;
    right: 0;
    top: 57.5%;
    text-align: center;
    font-family: "Tinos", "Times New Roman", serif;
    font-weight: 400;
    font-size: 24cqh;
    line-height: 1;
    letter-spacing: -0.01em;
  }

  .member-number {
    position: absolute;
    left: 0;
    right: 0;
    top: 81.2%;
    text-align: center;
    font-family: "Tinos", "Times New Roman", serif;
    font-weight: 700;
    font-size: 6cqh;
    line-height: 1;
  }
</style>
</head>
<body>
  <main class="card-set">

    <article class="vip-card vip-card--gold" aria-label="Golden VIP card">
      <div class="flourish-field" role="img" aria-label="Faint swirling floral pattern across the card"></div>
      <div class="ornament ornament--top" role="img" aria-label="Decorative scroll ornament"></div>
      <div class="brand-band">
        <span class="brand-dot"></span>
        <span class="brand-name">Bright Cove Leisure Plaza</span>
      </div>
      <div class="tier-mark">VIP</div>
      <div class="member-number">NO. 000001</div>
      <div class="ornament ornament--bottom" role="img" aria-label="Decorative scroll ornament"></div>
    </article>

    <article class="vip-card vip-card--platinum" aria-label="Platinum VIP card">
      <div class="flourish-field" role="img" aria-label="Faint swirling floral pattern across the card"></div>
      <div class="ornament ornament--top" role="img" aria-label="Decorative scroll ornament"></div>
      <div class="brand-band">
        <span class="brand-dot"></span>
        <span class="brand-name">Bright Cove Leisure Plaza</span>
      </div>
      <div class="tier-mark">VIP</div>
      <div class="member-number">NO. 000001</div>
      <div class="ornament ornament--bottom" role="img" aria-label="Decorative scroll ornament"></div>
    </article>

    <article class="vip-card vip-card--diamond" aria-label="Diamond VIP card">
      <div class="flourish-field" role="img" aria-label="Faint swirling floral pattern across the card"></div>
      <div class="ornament ornament--top" role="img" aria-label="Decorative scroll ornament"></div>
      <div class="brand-band">
        <span class="brand-dot"></span>
        <span class="brand-name">Bright Cove Leisure Plaza</span>
      </div>
      <div class="tier-mark">VIP</div>
      <div class="member-number">NO. 000001</div>
      <div class="ornament ornament--bottom" role="img" aria-label="Decorative scroll ornament"></div>
    </article>

  </main>
</body>
</html>
```